Bourbon label design for bourbon brand. Looking to freshen our current label.

I need a Bourbon label design for our rebranded Bourbon bottle. Label should include picture of our horse and our logo on the bottle. Front Label is 3.5 inches wide and 6 inches tall, back label is 4 inches tall and 3 inches wide. Back label can be a simple plain logo like the one in the brief. I have included a design of our current bottle and label. We want to stay close to the current color schemes but want a fresh rebrand of the design. The label needs to be the correct size on a tall bottle like pictured.

Target Market(s)

Our Bourbon members, 30-50 year old males

Requirements
Must have
• Picture of our horse, our B logo , straight Bourbon whiskey on the front. Room to edit text on the back label.

```html
<!DOCTYPE html>
<html lang="en">
<head>
<meta charset="utf-8">
<title>Midnight Cask Straight Bourbon Whiskey Labels</title>
<link rel="stylesheet" href="https://fonts.googleapis.com/css2?family=Alfa+Slab+One&family=Michroma&family=Arimo:wght@400;700&display=swap">
<style>
  :root {
    --bg: #e6e6e6;
    --label-black: #151515;
    --gold-light: #f3d77a;
    --gold: #c9a13a;
    --gold-dark: #8a6414;
    --white: #f4f4f4;
    --silver: #d9d9d9;
    --ink: #111111;
  }
  * { box-sizing: border-box; margin: 0; padding: 0; }
  html, body { width: 1200px; height: 912px; overflow: hidden; }
  body {
    background: var(--bg);
    font-family: "Arimo", Arial, sans-serif;
    display: flex;
    align-items: center;
    justify-content: center;
    gap: 80px;
  }

  /* ---------- Front label ---------- */
  .front-label {
    position: relative;
    width: 315px;
    height: 540px;
    background: var(--label-black);
    color: var(--white);
    display: flex;
    flex-direction: column;
    align-items: center;
  }
  .gold-band {
    position: absolute;
    left: 0; right: 0;
    height: 14px;
    display: flex;
    flex-direction: column;
    justify-content: space-between;
  }
  .gold-band span { display: block; background: linear-gradient(90deg, var(--gold-dark), var(--gold-light), var(--gold), var(--gold-light), var(--gold-dark)); }
  .gold-band span:first-child { height: 7px; }
  .gold-band span:last-child { height: 3px; }
  .gold-band.top { top: 18px; }
  .gold-band.bottom { bottom: 18px; flex-direction: column-reverse; }

  .brand-row {
    margin-top: 62px;
    display: flex;
    align-items: center;
    gap: 14px;
  }
  .est-tag {
    font-family: "Michroma", sans-serif;
    font-size: 9px;
    color: var(--gold);
    border-top: 1px solid var(--gold);
    border-bottom: 1px solid var(--gold);
    padding: 1px 3px;
  }
  .brand-name {
    display: flex;
    align-items: center;
    gap: 6px;
    font-family: "Michroma", sans-serif;
    font-size: 11px;
    line-height: 1.3;
    color: var(--gold);
    text-align: center;
  }
  .brand-dot { width: 10px; height: 10px; border-radius: 50%; background: var(--gold); }

  .horse-art {
    margin-top: 20px;
    width: 120px;
    height: 215px;
    border-radius: 50px 50px 20px 20px;
    background: radial-gradient(ellipse at 50% 40%, var(--gold-light) 0%, var(--gold) 45%, var(--gold-dark) 80%, var(--label-black) 100%);
  }

  .side-tag {
    position: absolute;
    top: 255px;
    font-family: "Arimo", sans-serif;
    font-size: 9px;
    line-height: 1.1;
    letter-spacing: 0.5px;
    text-align: center;
    color: var(--silver);
    border-bottom: 1px solid var(--silver);
    padding-bottom: 2px;
  }
  .side-tag.left { left: 18px; }
  .side-tag.right { right: 18px; }

  .title-straight {
    margin-top: 26px;
    font-family: "Michroma", sans-serif;
    font-size: 19px;
    letter-spacing: 3px;
    color: var(--white);
  }
  .title-bourbon {
    font-family: "Alfa Slab One", serif;
    font-size: 38px;
    line-height: 1.05;
    letter-spacing: 1px;
    color: var(--gold);
  }
  .title-whiskey {
    font-family: "Alfa Slab One", serif;
    font-size: 24px;
    letter-spacing: 2px;
    color: var(--white);
  }

  .spec-strip {
    position: absolute;
    left: 8px; right: 8px;
    bottom: 42px;
    height: 20px;
    background: linear-gradient(90deg, #bfbfbf, #f2f2f2, #c8c8c8);
    display: flex;
    align-items: stretch;
  }
  .spec-cell {
    flex: 1;
    font-size: 7px;
    line-height: 1.05;
    color: #333;
    padding: 2px 6px;
    border-right: 1px solid #666;
  }
  .spec-cell:last-child { border-right: 0; }

  /* ---------- Back label ---------- */
  .back-label {
    width: 270px;
    height: 360px;
    background: var(--label-black);
    color: var(--white);
    padding: 20px 14px 10px;
    display: flex;
    flex-direction: column;
    align-items: center;
    text-align: center;
  }
  .back-brand {
    display: flex;
    align-items: center;
    gap: 10px;
  }
  .back-brand .brand-dot { width: 28px; height: 28px; background: var(--white); }
  .back-brand-name {
    font-family: "Michroma", sans-serif;
    font-size: 13px;
    line-height: 1.15;
    letter-spacing: 1px;
    text-align: left;
  }
  .back-brand-name small {
    display: block;
    font-size: 6px;
    letter-spacing: 3px;
    border-top: 1px solid var(--white);
    margin-top: 2px;
    padding-top: 1px;
  }
  .edition {
    margin-top: 20px;
    font-size: 8px;
    font-weight: 700;
    line-height: 1.25;
  }
  .story {
    margin-top: 10px;
    font-size: 7px;
    line-height: 1.35;
  }
  .bottler {
    margin-top: 10px;
    font-size: 7px;
    line-height: 1.35;
  }
  .bottler strong { font-weight: 700; }
  .gov-warning {
    margin-top: auto;
    width: 100%;
    background: var(--white);
    color: var(--ink);
    font-size: 6.6px;
    line-height: 1.3;
    text-align: justify;
    padding: 4px 5px;
  }
</style>
</head>
<body>

  <section class="front-label" aria-label="Front label">
    <div class="gold-band top"><span></span><span></span></div>

    <div class="brand-row">
      <span class="est-tag">EST</span>
      <div class="brand-name"><span class="brand-dot"></span>MIDNIGHT<br>CASK</div>
      <span class="est-tag">2016</span>
    </div>

    <div class="horse-art" role="img" aria-label="Gold illustration of a racehorse and jockey galloping toward the viewer"></div>

    <div class="side-tag left">SINGLE<br>BARREL</div>
    <div class="side-tag right">CASK<br>STRENGTH</div>

    <div class="title-straight">STRAIGHT</div>
    <div class="title-bourbon">BOURBON</div>
    <div class="title-whiskey">WHISKEY</div>

    <div class="spec-strip">
      <div class="spec-cell">BARREL<br>NO.</div>
      <div class="spec-cell">AGED<br>YEARS</div>
      <div class="spec-cell">ALC<br>VOL.</div>
    </div>

    <div class="gold-band bottom"><span></span><span></span></div>
  </section>

  <section class="back-label" aria-label="Back label">
    <div class="back-brand">
      <span class="brand-dot"></span>
      <div class="back-brand-name">MIDNIGHT<br>CASK<small>COMPANY</small></div>
    </div>

    <p class="edition">Winners Series<br>Silver Tempest Edition<br>Single Barrel No.45</p>

    <p class="story">The Midnight Racing Winners Series honors the horses who have brought home victories for our stable. This edition celebrates Silver Tempest and her maiden victory on May 28, 2021.</p>

    <p class="story">Raise a glass to her incredible career with this non-chill filtered single barrel crafted in her honor. Here's to Silver Tempest — a true champion!</p>

    <p class="bottler">Bottled by Riverbend Whiskey Co., Louisville, Kentucky. Distilled in Bardstown, Kentucky<br><strong>MIDNIGHTCASK-GROUP.COM</strong><br>750 ml</p>

    <p class="gov-warning"><strong>GOVERNMENT WARNING:</strong> (1) According to the Surgeon General, women should not drink alcoholic beverages during pregnancy because of the risk of birth defects. (2) Consumption of alcoholic beverages impairs your ability to drive a car or operate machinery, and may cause health problems.</p>
  </section>

</body>
</html>
```